International business needs a web page design

We need a web page design for a new service that our new "sub-company" of our existing company will offer. We are based in Denmark, and our new "sub-company" is called 'Velkari'. The service we offer is automated server configuration and In-Depth monitoring, and optional operations support. Our monitoring has a lot of graphs (like those seen here: https://velkari.example/ with either black or white background ) and the website needs to communicate a sense of Security/safety and that our customers can relax, because we have the full overview of their service and servers. The website should not be with black background.

We deliver low price, high quality and professional operations - which we can do, because we automate it and have people with 15+ years of experience doing so.

We have attached :

Target Market(s)

Chief Technological officers (CTO's) and Developers (small business, run by developers) - who needs professional IT operations.

Industry/Entity Type

Business

Coding

Coded - Design and coding required

Number of Pages Required

3 page

Requirements
Must have
• Frontpage :
• A lot of visualization(some with people too) rather than a lot of text
• A short, describing text on front page telling what people get
• 3 steps showing people how it works. (Could be presented in a video placed on top of a big front image or perhaps with all 3 steps/pictures shown at the same time or perhaps in a completely different way).
Nice to have
• A big front image(perhaps a person with a cellphone showing graphs and a "all okay" message) with a text and the 3-steps pictures/or video on top of it
• 3 boxes under the front image/top of the site showing what benefits people get from the service
Should not have
• Not a black/dark site

```html
<!DOCTYPE html>
<html lang="en">
<head>
<meta charset="utf-8">
<title>Velkari – Instant server setup &amp; In-depth monitoring</title>
<link rel="stylesheet" href="https://fonts.googleapis.com/css2?family=Open+Sans:wght@400;600;700&display=swap">
<style>
  :root {
    --ink: #555555;
    --dark: #231f20;
    --brand: #1aa0d8;
    --drop-1: #35b0e0;
    --drop-2: #1f95c4;
    --btn-blue: #1a9ad6;
    --btn-green: #14c22c;
    --white: #ffffff;
    --band: rgba(40, 34, 30, 0.62);
    --footer: #222222;
    --footer-text: #e6e6e6;
    --icon-grey: #9a9a9a;
  }
  * { box-sizing: border-box; margin: 0; padding: 0; }
  html, body { width: 1200px; height: 1046px; overflow: hidden; }
  body { position: relative; font-family: "Open Sans", sans-serif; background: var(--white); color: var(--ink); }
  .abs { position: absolute; }

  /* Header */
  .site-header { position: absolute; left: 0; top: 0; width: 1200px; height: 108px; background: var(--white); border-bottom: 1px solid #e2e2e2; }
  .nav-link { position: absolute; top: 61px; font-size: 13px; color: var(--ink); text-decoration: none; }
  .nav-services { position: absolute; left: 283px; top: 54px; width: 144px; height: 40px; background: var(--dark); color: var(--white); font-size: 13px; padding: 7px 0 0 27px; }
  .dropdown { position: absolute; left: 283px; top: 93px; width: 144px; z-index: 3; }
  .dropdown a { display: block; height: 34px; padding: 9px 0 0 29px; font-size: 11px; color: var(--white); text-decoration: none; border-bottom: 1px solid #7fd0ee; }
  .dropdown a:first-child { background: var(--drop-1); height: 33px; }
  .dropdown a:last-child { background: var(--drop-2); }
  .brand { position: absolute; left: 477px; top: 25px; width: 260px; height: 60px; }
  .brand-mark { position: absolute; left: 0; top: 0; width: 58px; height: 58px; border-radius: 50%; background: var(--brand); }
  .brand-name { position: absolute; left: 66px; top: -6px; font-size: 38px; font-weight: 600; color: var(--dark); letter-spacing: -0.5px; }
  .brand-tag { position: absolute; left: 68px; top: 39px; font-size: 10px; color: var(--dark); white-space: nowrap; }

  /* Hero */
  .hero { position: absolute; left: 0; top: 108px; width: 1200px; height: 518px;
    background:
      radial-gradient(ellipse 260px 300px at 860px 230px, #c49a86 0%, rgba(180,130,100,0.6) 50%, rgba(0,0,0,0) 100%),
      radial-gradient(ellipse 300px 200px at 220px 120px, #f2b640 0%, rgba(230,160,40,0) 100%),
      linear-gradient(90deg, #8a7040 0%, #c49a45 25%, #d9a33c 40%, #7c6650 60%, #3c4a5e 90%, #2e3e52 100%); }
  .hero-title { position: absolute; left: 99px; top: 102px; font-size: 20.5px; font-weight: 600; color: var(--white); letter-spacing: 0.2px; }
  .hero-text { position: absolute; left: 99px; top: 145px; width: 342px; font-size: 11.5px; line-height: 19.7px; color: var(--white); text-align: justify; }
  .btn { position: absolute; top: 249px; height: 48px; color: var(--white); font-size: 12.5px; font-weight: 700; display: flex; align-items: center; justify-content: center; }
  .btn-setup { left: 99px; width: 202px; background: var(--btn-blue); }
  .btn-ok { left: 321px; width: 84px; background: var(--btn-green); }
  .slide-arrow { position: absolute; top: 209px; }
  .play { position: absolute; left: 561px; top: 221px; }

  .steps { position: absolute; left: 0; top: 402px; width: 1200px; height: 116px; background: var(--band); }
  .step-badge { position: absolute; top: 15px; width: 86px; height: 86px; border-radius: 50%; background: #f4f4f4; }
  .step-text { position: absolute; top: 36px; font-size: 15.5px; font-weight: 600; line-height: 24px; color: var(--white); }

  /* Benefits */
  .benefit { position: absolute; top: 660px; width: 311px; height: 264px; color: var(--white); text-align: center; }
  .benefit h3 { margin-top: 27px; font-size: 17px; font-weight: 600; line-height: 24px; }
  .benefit p { margin-top: 18px; font-size: 11px; line-height: 19.7px; }
  .b-fast { left: 99px; background: linear-gradient(160deg, #1d5f96 0%, #0f3a63 45%, #1b1b1f 70%, #1a5d94 100%); }
  .b-relax { left: 445px; background: linear-gradient(170deg, #8b9fba 0%, #5a6f8e 50%, #8394ac 100%); }
  .b-graphs { left: 789px; background: radial-gradient(circle at 175px 150px, #2f6db0 0%, #123c70 40%, #0a1f3c 100%); }

  /* Footer */
  .site-footer { position: absolute; left: 0; top: 953px; width: 1200px; height: 93px; background: var(--footer); color: var(--footer-text); font-size: 11.5px; }
  .footer-links { position: absolute; left: 99px; top: 25px; }
  .footer-copy { position: absolute; left: 99px; top: 51px; }
  .social { position: absolute; left: 1016px; top: 30px; display: flex; gap: 6px; }
  .social span { width: 14px; height: 14px; border-radius: 50%; background: var(--icon-grey); display: block; }
</style>
</head>
<body>

<header class="site-header">
  <a class="nav-link" style="left:99px">Home</a>
  <a class="nav-link" style="left:195px">About us</a>
  <div class="nav-services">Services</div>
  <div class="brand">
    <span class="brand-mark"></span>
    <span class="brand-name">Velkari</span>
    <span class="brand-tag">Instant server setup &amp; In-depth monitoring</span>
  </div>
  <a class="nav-link" style="left:868px">Blog</a>
  <a class="nav-link" style="left:956px">News</a>
  <a class="nav-link" style="left:1050px">Contact us</a>
</header>

<nav class="dropdown">
  <a>Service 1</a>
  <a>Service 2</a>
</nav>

<section class="hero" role="img" aria-label="Smiling man talking on his mobile phone against a warm blurred background">
  <h1 class="hero-title">PERSPICIATIS UNDE OMNIS ISTE NATUS</h1>
  <p class="hero-text">Must explain to you how all this mistaken idea of denouncing Pleasure and praising pain was born and I will give you a complete Account of the system, and expound the actual teachings of the Great explorer of the truth,</p>
  <a class="btn btn-setup">INSATNT SERVER SETUP NOW</a>
  <a class="btn btn-ok">ALL OK</a>

  <svg class="slide-arrow" style="left:30px" width="34" height="34" viewBox="0 0 34 34">
    <circle cx="17" cy="17" r="16" fill="none" stroke="#3a3020" stroke-width="1.3"/>
    <path d="M19 11 L13 17 L19 23" fill="none" stroke="#3a3020" stroke-width="1.3"/>
  </svg>
  <svg class="slide-arrow" style="left:1136px" width="34" height="34" viewBox="0 0 34 34">
    <circle cx="17" cy="17" r="16" fill="none" stroke="#f0d6b0" stroke-width="1.3"/>
    <path d="M15 11 L21 17 L15 23" fill="none" stroke="#f0d6b0" stroke-width="1.3"/>
  </svg>
  <svg class="play" width="78" height="78" viewBox="0 0 78 78">
    <circle cx="39" cy="39" r="36" fill="rgba(255,255,255,0.12)" stroke="rgba(255,255,255,0.75)" stroke-width="4"/>
    <path d="M30 24 L56 39 L30 54 Z" fill="rgba(255,255,255,0.75)"/>
  </svg>

  <div class="steps">
    <div class="step-badge" style="left:99px" role="img" aria-label="Phone with a tick message icon">
      <svg width="86" height="86" viewBox="0 0 86 86"><rect x="29" y="24" width="22" height="38" rx="4" fill="#2aa6d6"/><rect x="40" y="20" width="20" height="15" rx="3" fill="#f5c430"/><path d="M45 27 l3 3 l6 -6" fill="none" stroke="#fff" stroke-width="2"/></svg>
    </div>
    <div class="step-text" style="left:201px">STEP 1<br>CHOOSE PROFILE IMAGE</div>

    <div class="step-badge" style="left:516px" role="img" aria-label="Computer screen with cursor icon">
      <svg width="86" height="86" viewBox="0 0 86 86"><rect x="22" y="24" width="42" height="30" rx="3" fill="#2aa6d6"/><rect x="38" y="54" width="10" height="8" fill="#8a8a8a"/><path d="M44 34 l10 6 l-5 1 l3 6 l-3 1 l-3 -6 l-3 3 z" fill="#f2692b"/></svg>
    </div>
    <div class="step-text" style="left:619px">STEP 2<br>RUN COMMAND</div>

    <div class="step-badge" style="left:871px" role="img" aria-label="Presentation board with rising chart icon">
      <svg width="86" height="86" viewBox="0 0 86 86"><rect x="22" y="24" width="42" height="28" fill="#fff" stroke="#555" stroke-width="2"/><path d="M27 46 l9 -8 l7 5 l12 -12" fill="none" stroke="#e23b2e" stroke-width="3"/><path d="M43 52 v10 M36 64 l7 -8 l7 8" stroke="#555" stroke-width="2" fill="none"/></svg>
    </div>
    <div class="step-text" style="left:973px">STEP3<br>SERVER IS READY</div>
  </div>
</section>

<section class="benefit b-fast" role="img" aria-label="Rows of server racks on a blue grid floor">
  <h3>It's Fast And<br>Easy</h3>
  <p>We Have Done All the work,so you Can Focus on<br>what you need<br>out of your server- your server will be ready in a few<br>minutes.....(instant server setup)</p>
</section>

<section class="benefit b-relax" role="img" aria-label="Rows of computer monitors and keyboards in a blue-grey office">
  <h3>Relax And Rest<br>Assured</h3>
  <p>We Will moniter your server and are ready 24/7 to<br>handle issues on your<br>server- so you do not have to be the systems expert</p>
  <p style="margin-top:6px">We will advise and help you to ensure that you can<br>grow with your sucess,<br>and handle any emergency</p>
</section>

<section class="benefit b-graphs" role="img" aria-label="Server room with a glowing blue globe">
  <h3>You'll love your Detiled<br>Performance Graphs</h3>
  <p>We will tell you minute-by-minute- how your website<br>performs and how close your server<br>is to it's limits, so you can react your time</p>
</section>

<footer class="site-footer">
  <div class="footer-links">Home&nbsp;|&nbsp;About us&nbsp;|&nbsp;Server&nbsp;|&nbsp;Blog&nbsp;|&nbsp;News&nbsp;|&nbsp;Contact us</div>
  <div class="footer-copy">Copyrights@Company name.2014</div>
  <div class="social" aria-label="Social links">
    <span></span><span></span><span></span><span></span><span></span>
  </div>
</footer>

</body>
</html>
```